Modern/Bold/Unique Prenatal Vitamin label redesign

We are in need of a design update for our Prenatal Vitamin label. We want to modernize our label and give it a fresh feel.
It should bring a feeling of fun, joy, and sophistication, but also be bold/edgy/unique and portray Trust and Authority. Our buyers are mainly mothers in the age range of 25-34 who are pregnant or breastfeeding.
I will attach our current label design, as well as some inspiration to go off of.
We like the idea of having a clean, easy to read label label with bold/vibrant colors and fonts. We like the idea of having some retro vibes in it as well
Please see the attached artwork for design inspiration (New Design Idea). We like the idea of having a pregnant mother image like the attachment on the label, with the rest of the label being white. Please come up with a unique drawing/image for the design. We cannot use a copied image or stock image.
We look forward to working with you!

```html
<!DOCTYPE html>
<html lang="en">
<head>
<meta charset="utf-8">
<title>Nestling Care – Prenatal Bloom label</title>
<link href="https://fonts.googleapis.com/css2?family=Quicksand:wght@500;600;700&display=swap" rel="stylesheet">
<style>
  :root {
    --backdrop: #ef9aad;
    --label-white: #ffffff;
    --label-shade: #ececec;
    --ink-grey: #3f3f3f;
    --ink-dark: #2e2e2e;
    --accent-pink: #e6356f;
    --accent-pink-soft: #f06292;
    --art-blue: #2b6fd6;
    --art-magenta: #e23ab4;
    --art-red: #e2332b;
    --art-green: #7ccd2e;
    --art-teal: #1fb7c9;
  }
  * { box-sizing: border-box; margin: 0; padding: 0; }
  html, body {
    width: 1200px; height: 1172px; overflow: hidden;
    background: var(--backdrop);
  }
  .label {
    position: absolute; left: 82px; top: 71px;
    width: 1036px; height: 1030px;
    background: linear-gradient(90deg, var(--label-white) 0%, var(--label-white) 60%, var(--label-shade) 100%);
    font-family: "Quicksand", sans-serif;
  }
  .brand {
    position: absolute; left: 40px; top: 78px;
    color: var(--ink-grey); font-weight: 700; line-height: 0.95;
    letter-spacing: -1px;
  }
  .brand .line-one { display: block; font-size: 60px; }
  .brand .line-two { display: block; font-size: 84px; }
  .product-name {
    position: absolute; left: 36px; top: 372px;
    color: var(--accent-pink); font-weight: 700;
    font-size: 100px; line-height: 0.88; letter-spacing: -1px;
  }
  .rule-vertical {
    position: absolute; left: 40px; top: 580px;
    width: 3px; height: 200px; background: var(--accent-pink);
  }
  .rule-horizontal {
    position: absolute; left: 40px; top: 612px;
    width: 128px; height: 3px; background: var(--accent-pink);
  }
  .claims {
    position: absolute; left: 56px; top: 662px;
    color: var(--ink-grey); font-weight: 500; font-size: 20px;
    line-height: 1.5; text-transform: uppercase;
  }
  .claims .claim-strong {
    display: block; font-weight: 700; font-size: 26px;
    color: var(--ink-dark); line-height: 1.1;
  }
  .count-badge {
    position: absolute; left: 38px; top: 872px;
    width: 110px; height: 110px;
  }
  .badge-divider {
    position: absolute; left: 168px; top: 888px;
    width: 3px; height: 88px; background: var(--ink-grey);
  }
  .supplement-tag {
    position: absolute; left: 194px; top: 912px;
    color: var(--accent-pink); font-weight: 600; font-size: 26px;
    line-height: 1.05; text-transform: uppercase;
  }
  .mother-art {
    position: absolute; left: 560px; top: 30px;
    width: 450px; height: 1000px;
    border-radius: 220px 220px 0 0;
    background:
      radial-gradient(circle at 40% 20%, var(--art-teal) 0%, transparent 35%),
      radial-gradient(circle at 55% 40%, var(--art-green) 0%, transparent 30%),
      radial-gradient(circle at 35% 70%, var(--art-magenta) 0%, transparent 35%),
      radial-gradient(circle at 60% 85%, var(--art-red) 0%, transparent 35%),
      linear-gradient(160deg, var(--art-blue), var(--art-magenta) 55%, var(--art-red));
    opacity: 0.9;
  }
</style>
</head>
<body>
  <main class="label">
    <div class="brand">
      <span class="line-one">Nestling</span>
      <span class="line-two">Care</span>
    </div>

    <h1 class="product-name">Prenatal<br>Bloom</h1>

    <div class="rule-vertical"></div>
    <div class="rule-horizontal"></div>

    <p class="claims">
      Once daily<br>
      Premium multivitamin for
      <span class="claim-strong">Mama and baby</span>
    </p>

    <svg class="count-badge" viewBox="0 0 110 110" aria-label="90 veggie capsules">
      <defs>
        <path id="arc-top" d="M14,55 A41,41 0 0 1 96,55"/>
        <path id="arc-bottom" d="M10,55 A45,45 0 0 0 100,55"/>
      </defs>
      <text font-family="Quicksand, sans-serif" font-size="15" font-weight="600" fill="#e6356f">
        <textPath href="#arc-top" startOffset="50%" text-anchor="middle">VEGGIE</textPath>
      </text>
      <text font-family="Quicksand, sans-serif" font-size="14" font-weight="600" fill="#e6356f" dy="12">
        <textPath href="#arc-bottom" startOffset="50%" text-anchor="middle">CAPSULES</textPath>
      </text>
      <text x="55" y="70" text-anchor="middle" font-family="Quicksand, sans-serif" font-size="46" font-weight="600" fill="#3f3f3f">(90)</text>
    </svg>

    <div class="badge-divider"></div>
    <p class="supplement-tag">Dietary<br>Supplement</p>

    <div class="mother-art" role="img" aria-label="Colourful paint-splash silhouette of a pregnant mother in profile, releasing butterflies from her raised hand"></div>
  </main>
</body>
</html>
```